Card Design for my dog training business Rustpaw Obedience

Need a business card design for my dog training business with my new logo. Want the card to come off professional yet fun. Want it to be very eye catchy as well. I normally have these at vet clinics, pet stores, and groomers. so need it to look better than my competitors.
Target Market(s)
dog owners
Industry/Entity Type
Dog Training
Contact Information for Business Card
needs logo, my name and info
Font styles to use
Serif
Colors
0255a3
ffffff
ec1f27
000000
333333
fbfbfb
Requirements
Must have
- Rustpaw Obedience
- Hollis Brandt
- 415 903 2267
- info@rustpawobedience.example
- www.rustpawobedience.example

```html
<!DOCTYPE html>
<html lang="en">
<head>
<meta charset="utf-8">
<title>Rustpaw Obedience – Business Card</title>
<link rel="stylesheet" href="https://fonts.googleapis.com/css2?family=Libre+Baskerville:wght@400;700&display=swap">
<style>
  :root {
    --brand-blue: #0255a3;
    --paper: #ffffff;
    --canvas: #fbfbfb;
    --ink: #333333;
    --ink-dark: #000000;
    --muted: #666666;
  }
  * { box-sizing: border-box; margin: 0; padding: 0; }
  html, body {
    width: 1200px; height: 834px; overflow: hidden;
    background: var(--canvas);
    font-family: "Libre Baskerville", Georgia, serif;
  }
  .sheet {
    width: 1200px; height: 834px;
    display: flex; align-items: center; justify-content: center; gap: 40px;
  }
  .card {
    position: relative;
    width: 540px; height: 309px;
    overflow: hidden;
    box-shadow: 0 6px 22px rgba(0,0,0,.18);
  }
  /* Front */
  .card-front { background: var(--brand-blue); color: var(--paper); }
  .card-front .brand-mark {
    position: absolute; left: 50%; top: 44%;
    transform: translate(-50%, -50%);
    text-align: center;
    font-size: 30px; line-height: 1.2; font-weight: 400;
    color: var(--paper);
    white-space: nowrap;
  }
  .card-front .website {
    position: absolute; left: 34px; bottom: 26px;
    font-size: 15px; letter-spacing: .3px;
  }
  /* Back */
  .card-back { background: var(--brand-blue); }
  .card-back .brand-mark {
    position: absolute; left: 118px; top: 50%;
    transform: translate(-50%, -50%);
    text-align: center;
    font-size: 21px; line-height: 1.25; color: var(--paper);
    white-space: nowrap;
  }
  .card-back .info-panel {
    position: absolute; inset: 0;
    width: 100%; height: 100%;
  }
  .contact {
    position: absolute; left: 282px; top: 92px;
    color: var(--ink);
  }
  .contact .name {
    font-size: 17px; font-weight: 700; letter-spacing: 1px;
    text-transform: uppercase; color: var(--brand-blue);
  }
  .contact .role { font-size: 12px; color: var(--muted); margin-bottom: 18px; }
  .contact-list { list-style: none; }
  .contact-list li {
    display: flex; align-items: center; gap: 10px;
    font-size: 12px; margin-bottom: 9px; color: var(--ink);
  }
  .contact-icon {
    width: 18px; height: 18px; border-radius: 4px;
    background: var(--brand-blue);
    display: flex; align-items: center; justify-content: center;
    flex: none;
  }
</style>
</head>
<body>
<main class="sheet">
  <section class="card card-front" aria-label="Business card front">
    <div class="brand-mark">Rustpaw<br>Obedience</div>
    <div class="website">www.rustpawobedience.example</div>
  </section>

  <section class="card card-back" aria-label="Business card back">
    <div class="brand-mark">Rustpaw<br>Obedience</div>
    <svg class="info-panel" viewBox="0 0 540 309" aria-hidden="true">
      <polygon points="250,0 540,0 540,309 250,309 250,110 238,100 250,90" fill="var(--paper)"/>
    </svg>
    <div class="contact">
      <div class="name">Hollis Brandt</div>
      <div class="role">Owner</div>
      <ul class="contact-list">
        <li>
          <span class="contact-icon">
            <svg width="11" height="11" viewBox="0 0 24 24"><path fill="#fff" d="M6.6 10.8a15.1 15.1 0 0 0 6.6 6.6l2.2-2.2c.3-.3.7-.4 1-.2 1.1.4 2.3.6 3.6.6.6 0 1 .4 1 1V20c0 .6-.4 1-1 1A17 17 0 0 1 3 4c0-.6.4-1 1-1h3.5c.6 0 1 .4 1 1 0 1.3.2 2.5.6 3.6.1.3 0 .7-.2 1z"/></svg>
          </span>415 903 2267
        </li>
        <li>
          <span class="contact-icon">
            <svg width="11" height="11" viewBox="0 0 24 24"><rect x="2" y="5" width="20" height="14" rx="2" fill="none" stroke="#fff" stroke-width="2"/><path d="M3 6l9 7 9-7" fill="none" stroke="#fff" stroke-width="2"/></svg>
          </span>info@rustpawobedience.example
        </li>
        <li>
          <span class="contact-icon">
            <svg width="11" height="11" viewBox="0 0 24 24"><circle cx="12" cy="12" r="9" fill="none" stroke="#fff" stroke-width="2"/><path d="M3 12h18M12 3c3 3 3 15 0 18M12 3c-3 3-3 15 0 18" fill="none" stroke="#fff" stroke-width="1.6"/></svg>
          </span>www.rustpawobedience.example
        </li>
      </ul>
    </div>
  </section>
</main>
</body>
</html>
```